依頼詳細
①TOPページのデザイン案をご提案ください。
②採用させていただく可能性の高い方と、
下層ページ1ページ、採用サイト等別サイト2ページ分について
ご相談したいと考えております。

<サイト概要>
・4ページ分(トップページ、下層ページ、採用サイト等2サイト)
・レスポンシブ
・セミナー案内などを、wordpressで更新していきます。

<納品物>
デザインカンプ(PSD希望ですが、AIでも可)を納品してください。

<応募条件>
・継続依頼も検討しているため、連絡がスムーズな方。

<参考サイト>
・株式会社ペネムス・ヤカルト
http://www.pnm-example.co.jp/

上記サイトのように、ファーストビューに背景に動画をフルスクリーンで表示させるのを希望しています。

・ツクリエ採用サイト
https://www.tsukurie-example.jp/saiyou/service/business.html

<提供する素材>
・写真、ロゴ、サイト内で使用するテキスト
サイトURL
http://www.meadowpath-x.com/
ページ数
4ページ
希望イメージ
シンプル 複雑
単色 カラフル
暗い 明るい
日常 高級
遊び心 厳粛
未来的 伝統的
女性的 男性的
希望する色
設定なし
納品ファイル
• イラストレーター形式 (.ai)
• フォトショップ形式 (.psd)
補足説明
・イラストレーター、フォトショップ、どちらで作成していただいても構いません。最終的に、制作データ(ai or psd)で納品をしていただける方。
・クライアント企業とのコミュニケーションに慣れていて、細かい修正等に対応していただける方
提供する素材を添付させていただきますので、
こちらをご使用ください。

<提供する素材>
・写真、ロゴ、サイト内で使用するテキスト
募集の締め切りを延長しましたので、
引き続きご提案をお待ちしております。
■ 選んだ理由

私たちのイメージに一番近いデザインを出していただきました。
またこちらの意向を汲んでくださり、
今後も引き続きお願いしたいと感じましたので決めさせていただきました。

■ 提案者全員のお礼・コメント

皆様、数々のご提案をいただき、ありがとうございました。

```html
<!DOCTYPE html>
<html lang="ja">
<head>
<meta charset="utf-8">
<title>Meadowpath | 歯科医院専門コンサルティング</title>
<link href="https://fonts.googleapis.com/css2?family=Noto+Sans+JP:wght@400;500;700;900&family=Noto+Serif+JP:wght@200;400;600&family=Oswald:wght@400;500;600&display=swap" rel="stylesheet">
<style>
:root{
  --navy:#1f2a44;
  --ink:#333a44;
  --muted:#6b7280;
  --line:#d8dde3;
  --paper:#ffffff;
  --soft:#f3f5f7;
  --pink:#e8408f;
  --magenta:#d63ea8;
  --purple:#8a4fd8;
  --blue:#2f7fe0;
  --cyan:#23c6e8;
  --green:#3dbb5a;
  --lime:#8dd43a;
  --orange:#f28a1c;
  --yellow:#f7c51e;
}
*{box-sizing:border-box;margin:0;padding:0}
html,body{width:1200px;height:4564px;overflow:hidden}
body{font-family:"Noto Sans JP",sans-serif;color:var(--ink);background:var(--paper);font-size:13px;line-height:1.7}
.page{position:relative;width:1200px;height:4564px}

/* header */
.site-header{position:absolute;top:0;left:0;width:1200px;height:88px;background:#fff;display:flex;align-items:center;padding:0 0 0 24px;z-index:2}
.brand{display:flex;flex-direction:column}
.brand-name{font-family:"Noto Sans JP",sans-serif;font-weight:700;font-size:26px;color:var(--navy);line-height:1}
.brand-tag{font-size:9px;color:var(--muted);margin-top:4px}
.global-nav{display:flex;gap:28px;margin-left:auto;margin-right:26px;font-size:13px;font-weight:500;color:var(--navy)}
.header-contact{display:flex;align-items:stretch;height:88px}
.btn-contact{width:116px;background:var(--pink);color:#fff;display:flex;align-items:center;justify-content:center;font-size:13px;font-weight:700}
.header-tel{width:170px;background:var(--navy);color:#fff;display:flex;flex-direction:column;justify-content:center;align-items:center}
.header-tel small{font-size:9px;opacity:.8}
.header-tel strong{font-family:"Oswald",sans-serif;font-size:24px;font-weight:500;color:#ff7fb3;letter-spacing:.02em;line-height:1.1}

/* hero */
.hero{position:absolute;top:88px;left:0;width:1200px;height:432px;overflow:hidden}
.hero-media{position:absolute;inset:0;background:linear-gradient(110deg,#f0a04b 0%,#b58bd8 22%,#6d86e8 48%,#4aa7e6 75%,#2e6fc9 100%)}
.hero-copy{position:absolute;top:150px;left:0;width:100%;text-align:center;color:#fff;font-weight:700;font-size:34px;line-height:1.6;letter-spacing:.06em;text-shadow:0 2px 8px rgba(20,30,80,.35)}

/* intro */
.intro{position:absolute;top:520px;left:0;width:1200px;height:260px;background:#fff}
.intro-zero{position:absolute;left:40px;top:20px;font-family:"Noto Serif JP",serif;font-weight:200;font-size:220px;line-height:1;color:transparent;-webkit-text-stroke:2px #c9ced6}
.intro-arrow{position:absolute;left:176px;top:120px}
.intro-one{position:absolute;left:226px;top:20px;font-family:"Noto Serif JP",serif;font-weight:400;font-size:220px;line-height:1;color:var(--navy)}
.intro-body{position:absolute;left:320px;top:100px;width:840px}
.intro-title{font-family:"Noto Serif JP",serif;font-size:26px;font-weight:600;color:var(--navy);display:inline-block;margin-right:18px;vertical-align:middle}
.intro-text{display:inline;font-size:12px;color:var(--ink);vertical-align:middle}
.intro-rule{position:absolute;left:320px;top:160px;width:840px;height:1px;background:var(--line)}

/* section heading */
.sec-head{text-align:center}
.sec-head h2{font-family:"Oswald",sans-serif;font-weight:500;font-size:48px;letter-spacing:.06em;line-height:1.1;background:var(--grad);-webkit-background-clip:text;background-clip:text;color:transparent;display:inline-block}
.sec-head p{font-size:11px;letter-spacing:.2em;color:var(--sub)}

.btn{display:block;width:200px;height:38px;margin:0 auto;color:#fff;font-family:"Oswald",sans-serif;font-size:14px;letter-spacing:.1em;text-align:center;line-height:38px}
.btn-view{background:linear-gradient(90deg,var(--cyan),var(--blue))}
.btn-read{background:var(--pink);width:200px;margin:0}
.btn-orange{background:linear-gradient(90deg,var(--orange),var(--yellow))}

/* voice */
.voice{position:absolute;top:780px;left:0;width:1200px;height:620px;background:var(--soft)}
.voice .sec-head{--grad:linear-gradient(90deg,var(--blue),var(--purple));--sub:var(--blue);padding-top:60px}
.voice-grid{position:absolute;top:160px;left:0;width:1200px;height:360px;display:flex}
.voice-thumbs{width:540px;display:grid;grid-template-columns:1fr 1fr;grid-template-rows:1fr 1fr}
.voice-thumb{position:relative;background:linear-gradient(135deg,#2c7be0,#4fb4ec 60%,#6fc6f0)}
.voice-thumb:nth-child(2),.voice-thumb:nth-child(3){background:linear-gradient(135deg,#3b6fd6,#5a9de8 60%,#8ab8f0)}
.voice-no{position:absolute;top:6px;left:8px;font-family:"Oswald",sans-serif;color:#fff;font-size:18px}
.voice-cap{position:absolute;bottom:10px;left:14px;right:14px;color:#fff;font-size:11px;border-top:1px solid rgba(255,255,255,.6);padding-top:4px}
.voice-movie{flex:1;position:relative;background:linear-gradient(120deg,#6a4fc8,#4a8fe4 45%,#8fb8e6 80%,#c7d8ee)}
.voice-play{position:absolute;left:50%;top:50%;transform:translate(-50%,-50%)}
.voice .btn{position:absolute;top:544px;left:500px}

/* service */
.service{position:absolute;top:1400px;left:0;width:1200px;height:960px;background:#fff}
.service .sec-head{--grad:linear-gradient(90deg,var(--purple),var(--pink));--sub:var(--magenta);padding-top:56px}
.svc{position:absolute;width:1200px}
.svc-media{position:absolute;height:270px}
.svc-text{position:absolute;width:470px}
.svc-label{font-family:"Oswald",sans-serif;font-size:11px;color:var(--pink);letter-spacing:.1em}
.svc-title{font-size:20px;font-weight:700;color:var(--navy);margin:2px 0 8px;padding-left:12px;border-left:4px solid var(--pink);line-height:1.3}
.svc-desc{font-size:12px;color:var(--ink);margin-bottom:18px}
.svc-1{top:150px}
.svc-1 .svc-text{left:40px;top:20px}
.svc-1 .svc-media{left:560px;top:0;width:640px;background:linear-gradient(120deg,#9a6cd6,#c86fc4 45%,#e38bc0)}
.svc-2{top:430px}
.svc-2 .svc-media{left:0;top:0;width:600px;background:linear-gradient(120deg,#3c3f7a,#5b64b8 50%,#8a7ad2)}
.svc-2 .svc-text{left:640px;top:60px}
.svc-3{top:680px}
.svc-3 .svc-text{left:40px;top:30px}
.svc-3 .svc-media{left:560px;top:-10px;width:640px;height:280px;background:linear-gradient(120deg,#c45fbf,#e57fae 50%,#f2b0c4)}

/* blog */
.blog{position:absolute;top:2360px;left:0;width:1200px;height:560px;background:var(--soft)}
.blog .sec-head{--grad:linear-gradient(90deg,var(--green),var(--lime));--sub:var(--green);padding-top:34px}
.blog-list{position:absolute;top:130px;left:30px;width:1140px;display:flex;gap:20px}
.blog-card{width:270px;background:#fff}
.blog-thumb{height:170px;background:linear-gradient(135deg,#3aa55a,#7fcf6a 60%,#b9e08a)}
.blog-card:nth-child(2) .blog-thumb{background:linear-gradient(135deg,#5c7fa8,#8fb0cf)}
.blog-card:nth-child(3) .blog-thumb{background:linear-gradient(135deg,#4f6c8c,#9ab6cc)}
.blog-card:nth-child(4) .blog-thumb{background:linear-gradient(135deg,#6f8aa6,#b4c8da)}
.blog-body{padding:12px 14px 16px;font-size:12px;color:var(--navy);font-weight:500;line-height:1.6}
.blog-date{display:block;font-family:"Oswald",sans-serif;color:var(--green);font-size:11px;margin-bottom:2px}
.blog .btn{position:absolute;top:470px;left:500px}

/* recruit */
.recruit{position:absolute;top:2920px;left:0;width:1200px;height:700px;background:#fff}
.recruit .sec-head{--grad:linear-gradient(90deg,var(--orange),var(--yellow));--sub:var(--orange);padding-top:56px}
.recruit-band{position:absolute;top:140px;left:0;width:1200px;height:460px;background:linear-gradient(100deg,#e9a21a,#f4c430 40%,#f3b62a 70%,#e38a1c)}
.recruit-copy{position:absolute;top:150px;left:0;width:100%;text-align:center;color:#fff}
.recruit-copy h3{font-size:50px;font-weight:900;letter-spacing:.06em;line-height:1.3;text-shadow:0 2px 8px rgba(120,60,0,.35)}
.recruit-copy h3 span{font-size:76px}
.recruit-copy p{font-size:26px;font-weight:700;letter-spacing:.08em;text-shadow:0 2px 6px rgba(120,60,0,.35)}
.recruit .btn{position:absolute;top:632px;left:500px}

/* message */
.message{position:absolute;top:3620px;left:0;width:1200px;height:340px;background:#fff}
.message-text{position:absolute;left:40px;top:40px;width:720px}
.message-text h3{font-size:28px;font-weight:900;color:var(--blue);line-height:1.35}
.message-text h4{font-size:20px;font-weight:700;color:var(--blue);margin-bottom:14px}
.message-text p{font-size:12px;color:var(--ink);margin-bottom:24px}
.message-text .btn{background:linear-gradient(90deg,var(--blue),var(--cyan));margin:0}
.message-photo{position:absolute;left:800px;top:0;width:330px;height:340px;background:linear-gradient(160deg,#e7eaee,#c7ccd3 70%,#9aa3ae)}
.message-name{position:absolute;left:1138px;top:14px;writing-mode:vertical-rl;font-family:"Oswald",sans-serif;font-size:22px;letter-spacing:.14em;color:var(--navy)}

/* map */
.access-map{position:absolute;top:3960px;left:0;width:1200px;height:420px;background:linear-gradient(135deg,#eef0ec,#e2e6e0 50%,#eceee9)}
.map-pin{position:absolute;left:584px;top:150px}

/* footer */
.site-footer{position:absolute;top:4380px;left:0;width:1200px;height:150px;background:#fff;border-top:1px solid var(--line)}
.footer-brand{position:absolute;left:40px;top:40px;display:flex;align-items:center;gap:10px}
.footer-brand i{width:18px;height:18px;border-radius:50%;background:var(--green);display:block}
.footer-brand b{font-size:24px;font-weight:700;color:var(--navy)}
.footer-nav{position:absolute;left:240px;top:30px;display:flex;gap:40px;font-size:11px;color:var(--navy)}
.footer-nav ul{list-style:none}
.footer-nav li.sub{font-size:10px;color:var(--muted);padding-left:8px}
.footer-cta{position:absolute;right:40px;top:34px;width:200px}
.footer-cta .btn-contact{width:200px;height:34px;font-size:12px}
.footer-cta strong{display:block;margin-top:6px;font-family:"Oswald",sans-serif;font-size:26px;color:var(--pink);text-align:center;font-weight:500}
.copyright{position:absolute;top:4530px;left:0;width:1200px;height:34px;background:var(--navy);color:#c9d1de;font-size:10px;text-align:center;line-height:34px}
</style>
</head>
<body>
<div class="page">

<header class="site-header">
  <div class="brand">
    <span class="brand-name">Meadowpath</span>
    <span class="brand-tag">歯科医院専門コンサルティング</span>
  </div>
  <nav class="global-nav">
    <span>会社概要</span><span>サービス</span><span>クライアントの声</span><span>会社沿革</span><span>採用情報</span>
  </nav>
  <div class="header-contact">
    <a class="btn-contact">お問い合わせ</a>
    <div class="header-tel"><small>歯科医院様専用ダイヤル</small><strong>0120-418-207</strong></div>
  </div>
</header>

<section class="hero">
  <div class="hero-media" role="img" aria-label="セミナー会場で講演する講師と会場の様子の映像"></div>
  <p class="hero-copy">クライアントの “こうしたい” に<br>“そこまでやるか” でカタチにする</p>
</section>

<section class="intro">
  <div class="intro-zero">0</div>
  <svg class="intro-arrow" width="48" height="28" viewBox="0 0 48 28"><path d="M2 4l10 10-10 10M16 4l10 10-10 10M30 4l10 10-10 10" fill="none" stroke="#1f2a44" stroke-width="3"/></svg>
  <div class="intro-one">1</div>
  <div class="intro-body">
    <h3 class="intro-title">0から1を生み出せる</h3>
    <p class="intro-text">スキルや想いをもった仲間が集まり、挑戦を続けることで新しい価値を生み出します。<br>同じような悩みに、寄り添いながら一緒に考え抜くことで、歯科医院の未来をカタチにしていきます。</p>
  </div>
  <div class="intro-rule"></div>
</section>

<section class="voice">
  <div class="sec-head"><h2>VOICE</h2><p>クライアントの声</p></div>
  <div class="voice-grid">
    <div class="voice-thumbs">
      <div class="voice-thumb" role="img" aria-label="歯科医院の院長インタビュー写真"><span class="voice-no">01</span><span class="voice-cap">しらたま歯科医院　院長先生の声</span></div>
      <div class="voice-thumb" role="img" aria-label="歯科医院の院長インタビュー写真"><span class="voice-no">02</span><span class="voice-cap">みなと歯科クリニック　院長先生の声</span></div>
      <div class="voice-thumb" role="img" aria-label="歯科医院の院長インタビュー写真"><span class="voice-no">03</span><span class="voice-cap">あおば歯科医院　院長先生の声</span></div>
      <div class="voice-thumb" role="img" aria-label="歯科医院の院長インタビュー写真"><span class="voice-no">04</span><span class="voice-cap">さくら歯科医院　院長先生の声</span></div>
    </div>
    <div class="voice-movie" role="img" aria-label="講演する講師のインタビュー動画">
      <svg class="voice-play" width="70" height="70" viewBox="0 0 70 70"><circle cx="35" cy="35" r="33" fill="#8a4fd8" opacity=".9"/><path d="M28 22l20 13-20 13z" fill="#fff"/></svg>
    </div>
  </div>
  <a class="btn btn-view">VIEW ALL</a>
</section>

<section class="service">
  <div class="sec-head"><h2>SERVICE</h2><p>サービス</p></div>
  <div class="svc svc-1">
    <div class="svc-text">
      <span class="svc-label">CONSULTING</span>
      <h3 class="svc-title">歯科医院専門コンサルティング</h3>
      <p class="svc-desc">医院の現状（経営・人材採用・集患）を把握した上で、医院ごとに合わせたオーダーメイドのプログラムを提案します。</p>
      <a class="btn btn-read">READ MORE</a>
    </div>
    <div class="svc-media" role="img" aria-label="院内で打ち合わせをするスタッフの写真"></div>
  </div>
  <div class="svc svc-2">
    <div class="svc-media" role="img" aria-label="パソコンでホームページを制作する作業風景"></div>
    <div class="svc-text">
      <span class="svc-label">WEB SITE</span>
      <h3 class="svc-title">ホームページ作成</h3>
      <p class="svc-desc">歯科医院運営のノウハウを活かし、医院の強みが伝わるホームページを制作します。公開後の更新や集患までしっかりサポートします。</p>
      <a class="btn btn-read">READ MORE</a>
    </div>
  </div>
  <div class="svc svc-3">
    <div class="svc-text">
      <span class="svc-label">COMMUNITY</span>
      <h3 class="svc-title">歯科塾（歯科塾の仕組みとは？）</h3>
      <p class="svc-desc">同じ悩みを持つ院長先生が集まり、学び合い、成長するための場です。たくさんの成功事例を共有し、明日から使える知識を得られます。</p>
      <a class="btn btn-read">READ MORE</a>
    </div>
    <div class="svc-media" role="img" aria-label="子どもの歯科診療の様子の写真"></div>
  </div>
</section>

<section class="blog">
  <div class="sec-head"><h2>BLOG</h2><p>ブログ</p></div>
  <div class="blog-list">
    <article class="blog-card"><div class="blog-thumb" role="img" aria-label="第37回セミナーの告知画像"></div><div class="blog-body"><span class="blog-date">2017.07.27</span>歯科塾（第37回）「経営者の右腕が育つ、医院が伸びる」</div></article>
    <article class="blog-card"><div class="blog-thumb" role="img" aria-label="スーツ姿の参加者の写真"></div><div class="blog-body"><span class="blog-date">2017.07.20</span>歯科塾（第2回）「経営者の右腕が育つ、医院が伸びる」</div></article>
    <article class="blog-card"><div class="blog-thumb" role="img" aria-label="セミナー会場の写真"></div><div class="blog-body"><span class="blog-date">2017.07.13</span>歯科塾（第2回）「経営者の右腕が育つ、医院が伸びる」</div></article>
    <article class="blog-card"><div class="blog-thumb" role="img" aria-label="講義を聞く参加者の写真"></div><div class="blog-body"><span class="blog-date">2017.07.06</span>歯科塾（第2回）「経営者の右腕が育つ、医院が伸びる」</div></article>
  </div>
  <a class="btn btn-view">VIEW ALL</a>
</section>

<section class="recruit">
  <div class="sec-head"><h2>RECRUIT</h2><p>採用情報</p></div>
  <div class="recruit-band" role="img" aria-label="社員が集う職場の写真に黄色のトーン"></div>
  <div class="recruit-copy">
    <h3>一緒に「<span>翔</span>」ぼう！</h3>
    <p>あなたが動けば、世界も動き出す</p>
  </div>
  <a class="btn btn-orange">READ MORE</a>
</section>

<section class="message">
  <div class="message-text">
    <h3>「困っている人を助けたい」</h3>
    <h4>そんな想いでメドウパスは始まった。</h4>
    <p>クライアントの声を聞き、院長先生に寄り添いながら共に歩んできました。歯科医院専門のコンサルティングを通じて、患者様・スタッフ・地域のすべてが笑顔になる医院づくりを支えています。クライアントにとって最適な答えを追い求め、これからも挑戦を続けていきます。</p>
    <a class="btn">READ MORE</a>
  </div>
  <div class="message-photo" role="img" aria-label="代表者のポートレート写真"></div>
  <div class="message-name">KENJI MORISAWA</div>
</section>

<section class="access-map" role="img" aria-label="会社所在地周辺の地図">
  <svg class="map-pin" width="32" height="44" viewBox="0 0 32 44"><path d="M16 1C8 1 1 7 1 15c0 11 15 28 15 28s15-17 15-28C31 7 24 1 16 1z" fill="#e8408f"/><circle cx="16" cy="15" r="6" fill="#fff"/></svg>
</section>

<footer class="site-footer">
  <div class="footer-brand"><i></i><b>Meadowpath</b></div>
  <nav class="footer-nav">
    <ul><li>TOP</li></ul>
    <ul><li>サービス</li><li class="sub">歯科医院専門コンサルティング</li><li class="sub">ホームページ作成</li><li class="sub">歯科塾</li></ul>
    <ul><li>会社概要</li><li class="sub">代表メッセージ</li><li class="sub">会社沿革</li></ul>
    <ul><li>採用情報</li><li class="sub">募集要項</li></ul>
    <ul><li>クライアントの声</li></ul>
  </nav>
  <div class="footer-cta"><a class="btn-contact">お問い合わせ</a><strong>0120-418-207</strong></div>
</footer>
<div class="copyright">© Meadowpath Co.,Ltd. All Right Reserved.</div>

</div>
</body>
</html>
```